Pimbrox

Squarespace website for specialty health based ingredients, like organic Galactose, CBD Oil, Hyaluronic Acid. Already have a logo that I want to use.
Updates

Reason: Too few designs submitted. I would like to see what other designers can do.

I am not sure that I am getting what I need. I was hoping for a fully working Squarespace Website and listed that as uncoded. But, I think that it has to be fully coded and then I import it to my SquareSpace to get the functional website and request that Orvanix hosts the site. I mentioned that I want my office to be able to make revisions, etc but they will not know HTML nor be able convert it themselves. May I get an explanation? I do see several designs that I really like. But, am unclear exactly what I am purchasing and will eventually own.

Target Market(s)

Buyers of bulk chemicals used in the manufacture of pharmaceuticals, supplements, specialty foods and beverages.

Industry/Entity Type

Health And Wellness

Number of Pages Required

5+ page

Font styles to use
Sans Serif

Colors
33b8a4
add136
34a7d8

Requirements
Must have
• Please see Quillmere Fathom, Inc website for the pages that I need. I want a similar set up for products, only for specialty usually plant-based chemicals. Mapping should be the same.
Nice to have
• Brief content on a sample product such as pure CBD Oil or Galactose (D+) as examples. I would like a SquareSpace design if possible so that my staff can make changes readily. Would like to have Orvanix host the site once completed. Not sure what is Uncoded web design vs.Coded. Please help me know how to answer that question.
Should not have
• Please no association with Marijuana. This CBD Hemp Oil is 99.9% free of THC and imported into the United States legally. No people, needles, social networking, or newsletter necessary. Most of the designs are very tiny logos, could be bigger.

```html
<!DOCTYPE html>
<html lang="en">
<head>
<meta charset="utf-8">
<title>Pimbrox Inc. – Specialty Health Based Ingredients</title>
<link href="https://fonts.googleapis.com/css2?family=Lato:ital,wght@0,400;0,700;0,900;1,400;1,700;1,900&family=Montserrat:wght@500;600;700&display=swap" rel="stylesheet">
<style>
:root{
  --blue:#1d5b94;
  --green:#7aad3a;
  --ink:#1f1f1f;
  --text:#3a3a3a;
  --muted:#8a8a8a;
  --line:#d9d9d9;
  --panel:#f1f1f1;
  --dark:#262626;
  --darker:#1b1b1b;
  --white:#ffffff;
}
*{box-sizing:border-box;margin:0;padding:0}
html,body{width:668px;height:1200px;overflow:hidden;background:var(--white)}
body{font-family:"Lato",sans-serif;color:var(--text);position:relative}
.abs{position:absolute}

/* header */
.site-header{position:absolute;left:0;top:0;width:668px;height:66px;background:linear-gradient(#fff,#f4f4f4)}
.brand{position:absolute;left:55px;top:14px;display:flex;align-items:center;gap:7px}
.brand-mark{width:30px;height:30px;background:var(--green)}
.brand-name{font-family:"Lato",sans-serif;font-weight:900;font-size:27px;color:var(--blue);letter-spacing:-.3px}
.top-email{position:absolute;left:498px;top:11px;display:flex;align-items:center;gap:6px;font-size:9px;color:var(--ink)}
.main-nav{position:absolute;top:39px;left:326px;display:flex;gap:0}
.main-nav a{font-size:8.5px;font-weight:700;color:var(--ink);text-decoration:none;height:17px;line-height:17px;padding:0 6px;margin-right:8px;border-radius:2px}
.main-nav a.is-active{background:#2f2f2f;color:#fff}

/* hero */
.hero{position:absolute;left:0;top:66px;width:668px;height:262px;
  background:radial-gradient(ellipse at 55% 45%,#d9a58c 0 12%,transparent 30%),
  linear-gradient(180deg,#8c8a52 0%,#a88a4c 30%,#9aa244 65%,#6e8a2a 100%)}
.hero-arrow{position:absolute;top:120px;width:20px;height:20px;border-radius:50%;background:rgba(30,30,30,.7)}
.hero-caption{position:absolute;left:0;top:231px;width:668px;height:31px;background:rgba(20,20,20,.72);
  color:#fff;font-weight:900;font-style:italic;font-size:17px;text-align:center;line-height:31px;letter-spacing:.3px}

/* products */
.section-title{font-family:"Montserrat",sans-serif;font-weight:600;color:var(--ink)}
.section-title .accent-blue{color:var(--blue)}
.section-title .accent-green{color:var(--green)}
.products-title{position:absolute;top:346px;width:668px;text-align:center;font-size:16px}
.title-divider{position:absolute;top:383px;left:229px;width:210px;height:1px;background:var(--line)}
.title-divider-mark{position:absolute;top:375px;left:327px;width:14px;height:14px;background:var(--green);border:2px solid var(--blue)}
.product-card{position:absolute;top:405px;width:177px;height:141px;border:2px solid #cfcfcf;background:#fff;box-shadow:0 3px 4px rgba(0,0,0,.12)}
.product-photo{position:absolute;left:0;top:0;width:173px;height:117px}
.product-label{position:absolute;left:0;bottom:0;width:173px;height:20px;background:#3a3a3a;color:#fff;
  font-weight:900;font-size:9.5px;text-align:center;line-height:20px;letter-spacing:.6px}

/* welcome */
.welcome{position:absolute;left:0;top:577px;width:668px;height:188px;background:linear-gradient(#ececec,#f8f8f8)}
.welcome-brand{position:absolute;left:57px;top:70px;font-weight:900;font-size:30px;color:var(--blue);display:flex;align-items:center;gap:8px}
.welcome-brand-mark{width:26px;height:26px;background:var(--green)}
.welcome-rule{position:absolute;left:219px;top:33px;width:1px;height:135px;background:#c9c9c9}
.welcome-title{position:absolute;left:240px;top:31px;font-size:16px}
.welcome-underline{position:absolute;left:240px;top:55px;width:372px;height:1px;background:var(--line)}
.welcome-copy{position:absolute;left:240px;top:65px;width:374px;font-size:7.4px;line-height:10.8px;color:var(--ink)}
.welcome-copy p+p{margin-top:10px}
.read-more{position:absolute;left:240px;top:149px;width:72px;height:17px;border:1.5px solid var(--green);border-radius:9px;background:var(--green);
  color:#fff;font-size:7.5px;font-weight:700;line-height:14px;padding-left:7px}
.read-more i{position:absolute;right:1px;top:1px;width:13px;height:12px;border-radius:50%;background:#fff}

/* testimonials */
.testimonials-title{position:absolute;left:55px;top:793px;font-size:14px}
.testimonials-rule{position:absolute;left:55px;top:818px;width:370px;height:1px;background:var(--line)}
.testimonial{position:absolute;left:55px;width:372px;height:70px}
.avatar{position:absolute;left:1px;top:0;width:46px;height:50px}
.client-name{position:absolute;left:0;top:54px;width:48px;text-align:center;font-size:7px;font-weight:700;color:var(--ink)}
.quote{position:absolute;left:60px;top:10px;width:310px;font-size:6.9px;font-style:italic;line-height:11.5px;color:var(--ink)}
.quote b{color:#c8c8c8;font-size:13px;font-style:normal;line-height:0}

/* inquiry */
.inquiry{position:absolute;left:437px;top:792px;width:176px;height:183px;border:1px solid #dcdcdc;background:#fff;box-shadow:0 3px 5px rgba(0,0,0,.1)}
.inquiry-head{position:absolute;left:-1px;top:-1px}
.inquiry-title{position:absolute;left:0;top:3px;width:176px;text-align:center;font-family:"Montserrat",sans-serif;font-weight:600;color:#fff;font-size:14px}
.field{position:absolute;left:10px;width:156px;height:19px;border:1px solid #cfcfcf;border-radius:2px;background:linear-gradient(#f4f4f4,#fff);
  font-size:7.2px;color:var(--ink);padding-left:27px;line-height:17px}
.field::before{content:"";position:absolute;left:20px;top:2px;width:1px;height:13px;background:#d6d6d6}
.field svg{position:absolute;left:5px;top:4px}
.field-message{height:34px}
.submit{position:absolute;left:10px;top:156px;width:48px;height:15px;background:var(--green);color:#fff;font-size:8px;font-weight:900;text-align:center;line-height:15px}

/* footer */
.site-footer{position:absolute;left:0;top:999px;width:668px;height:172px;background:var(--dark)}
.footer-col-title{position:absolute;top:27px;font-family:"Montserrat",sans-serif;font-weight:600;font-size:10px;color:#fff}
.footer-col-title span{color:var(--green)}
.footer-rule{position:absolute;top:45px;height:1px;background:#444}
.footer-rule::before{content:"";position:absolute;left:0;top:0;width:20px;height:1px;background:var(--green)}
.footer-sep{position:absolute;top:45px;width:4px;height:110px;background:#1f1f1f}
.quick-links{position:absolute;left:55px;top:60px;list-style:none}
.quick-links li{font-size:7.5px;color:#bbb;height:20px}
.quick-links li::before{content:"›";color:var(--green);margin-right:4px}
.quick-links li.is-current{color:var(--green)}
.contact-name{position:absolute;left:159px;top:56px;font-weight:700;font-size:10px;color:#fff}
.contact-addr{position:absolute;left:159px;top:73px;font-size:7.4px;line-height:11px;color:#c9c9c9}
.contact-row{position:absolute;left:159px;font-size:7.4px;color:#c9c9c9;display:flex;align-items:center;gap:8px}
.map{position:absolute;left:321px;top:59px;width:143px;height:86px;background:linear-gradient(135deg,#dfe6c9,#b8cbe3 55%,#e9d7a8);border:2px solid #fff}
.footer-brand{position:absolute;left:497px;top:112px;font-weight:900;font-size:22px;color:#8f8f8f;display:flex;align-items:center;gap:6px}
.footer-brand-mark{width:20px;height:20px;background:#8f8f8f}
.bottom-bar{position:absolute;left:0;top:1171px;width:668px;height:29px;background:var(--darker);font-size:7.5px;color:#ddd}
.copyright{position:absolute;left:55px;top:10px}
.follow{position:absolute;left:484px;top:10px}
.social{position:absolute;top:5px;width:19px;height:19px;border-radius:50%;border:1.5px solid #fff}
</style>
</head>
<body>

<header class="site-header">
  <div class="brand"><span class="brand-mark"></span><span class="brand-name">Pimbrox</span></div>
  <div class="top-email">
    <svg width="18" height="18" viewBox="0 0 18 18"><polygon points="9,1 16,5 16,13 9,17 2,13 2,5" fill="#fff" stroke="#1d5b94" stroke-width="1.5"/><rect x="5" y="6.5" width="8" height="5.5" fill="#7aad3a"/><polyline points="5,6.5 9,9.5 13,6.5" fill="none" stroke="#fff" stroke-width=".8"/></svg>
    info@pimbroxinc.com
  </div>
  <nav class="main-nav">
    <a class="is-active">Home</a><a>About Us</a><a>Our Products</a><a>Testimonials</a><a>Contact Us</a>
  </nav>
</header>

<section class="hero" role="img" aria-label="Photo of a woman doing a side stretch on grass in a sunlit park">
  <span class="hero-arrow" style="left:35px"></span>
  <span class="hero-arrow" style="left:613px"></span>
  <div class="hero-caption">WE ARE A SPECIALTY HEALTH BASED INGREDIENTS FIRM.</div>
</section>

<h2 class="section-title products-title">Our <span class="accent-blue">Products</span></h2>
<div class="title-divider"></div>
<div class="title-divider-mark"></div>

<article class="product-card" style="left:55px">
  <div class="product-photo" role="img" aria-label="Photo of a white supplement bottle of organic galactose" style="background:radial-gradient(ellipse at 50% 50%,#cfe3dc 0 22%,#f4f4f4 45%,#fff 70%)"></div>
  <div class="product-label">ORGANIC GALACTOSE</div>
</article>
<article class="product-card" style="left:247px">
  <div class="product-photo" role="img" aria-label="Photo of an amber dropper bottle of CBD oil" style="background:radial-gradient(ellipse at 50% 55%,#a4561f 0 14%,#f3f3f3 38%,#fff 70%)"></div>
  <div class="product-label">CBD OIL</div>
</article>
<article class="product-card" style="left:437px">
  <div class="product-photo" role="img" aria-label="Photo of a pump bottle of hyaluronic cream" style="background:radial-gradient(ellipse at 50% 50%,#c9dbe8 0 20%,#f4f4f4 42%,#fff 70%)"></div>
  <div class="product-label">HYALURONIC ACID</div>
</article>

<section class="welcome">
  <div class="welcome-brand"><span class="welcome-brand-mark"></span>Pimbrox</div>
  <div class="welcome-rule"></div>
  <h2 class="section-title welcome-title">Welcome To <span class="accent-blue">Pimbrox Inc.</span></h2>
  <div class="welcome-underline"></div>
  <div class="welcome-copy">
    <p>Lorem ipsum dolor sit amet, consectetuer adipiscing elit, sed diam nonummy nibh euismod tincidunt ut laoreet dolore magna aliquam erat volutpat. Ut wisi enim ad minim veniam, quis nostrud exerci tation. um iriure dolor in hendrerit in vulputate velit esse molestie consequat, vel illu.</p>
    <p>Duis autem vel eum iriure dolor in hendrerit in vulputate velit esse molestie consequat, vel illum dolore eu feugiat nulla facilisis at vero eros et accumsan et iusto odio dignissim qui blandit praesent luptatum zzril delenit augue duis dolore te feugait nulla facilisi.</p>
  </div>
  <div class="read-more">READ MORE<i></i></div>
</section>

<h2 class="section-title testimonials-title"><span class="accent-blue">Client</span> <span class="accent-green">Testimonials</span></h2>
<div class="testimonials-rule"></div>

<div class="testimonial" style="top:827px">
  <svg class="avatar" viewBox="0 0 46 50" role="img" aria-label="Portrait photo of a male client"><polygon points="23,1 44,13 44,37 23,49 2,37 2,13" fill="#c9b3a0" stroke="#7aad3a" stroke-width="2"/></svg>
  <div class="client-name">MR. QUIS</div>
  <p class="quote"><b>“</b> Utm tellus dolor, dapibus eget, elemen velmki cursuser eleifelita amanokmn auctorbni wisi etereeri urnam. Lorem werrr ipsum dolor sit amet, conse ctetur adipisc ngop elit. Nullae in sollicitudin velitewrer bibendum velit.Cras vel facilisis ipsum, et venenat risus. <b>”</b></p>
</div>
<div class="testimonial" style="top:905px">
  <svg class="avatar" viewBox="0 0 46 50" role="img" aria-label="Portrait photo of a female client"><polygon points="23,1 44,13 44,37 23,49 2,37 2,13" fill="#d4b49a" stroke="#7aad3a" stroke-width="2"/></svg>
  <div class="client-name">MISS. QUIS</div>
  <p class="quote"><b>“</b> Utm tellus dolor, dapibus eget, elemen velmki cursuser eleifelita amanokmn auctorbni wisi etereeri urnam. Lorem werrr ipsum dolor sit amet, conse ctetur adipisc ngop elit. Nullae in sollicitudin velitewrer bibendum velit.Cras vel facilisis ipsum, et venenat risus. <b>”</b></p>
</div>

<form class="inquiry">
  <svg class="inquiry-head" width="178" height="34" viewBox="0 0 178 34"><polygon points="0,0 178,0 178,26 89,34 0,26" fill="#7aad3a"/><polygon points="0,0 178,0 178,22 89,30 0,22" fill="#1d5b94"/></svg>
  <div class="inquiry-title">Quick Inquiry</div>
  <div class="field" style="top:43px"><svg width="11" height="11" viewBox="0 0 11 11"><circle cx="5.5" cy="3.5" r="2.5" fill="#bbb"/><path d="M1 11a4.5 4 0 0 1 9 0z" fill="#bbb"/></svg>Name</div>
  <div class="field" style="top:67px"><svg width="11" height="11" viewBox="0 0 11 11"><rect x="1" y="3" width="9" height="6" fill="#bbb"/><polyline points="1,3 5.5,6.5 10,3" fill="none" stroke="#fff" stroke-width=".8"/></svg>Email Address</div>
  <div class="field" style="top:91px"><svg width="11" height="11" viewBox="0 0 11 11"><path d="M2 1l2 0 1 3-1.5 1a6 6 0 0 0 3 3L7.5 6.5l3 1 0 2c-5 1-9.5-3.5-8.5-8.5z" fill="#bbb"/></svg>Phone</div>
  <div class="field field-message" style="top:115px"><svg width="11" height="11" viewBox="0 0 11 11"><rect x="1" y="2" width="8" height="8" fill="none" stroke="#bbb"/><path d="M5 7l5-5" stroke="#bbb" stroke-width="1.3"/></svg>Message</div>
  <div class="submit">SUBMIT</div>
</form>

<footer class="site-footer">
  <h3 class="footer-col-title" style="left:55px">QUICK <span>LINKS</span></h3>
  <div class="footer-rule" style="left:55px;width:72px"></div>
  <ul class="quick-links">
    <li class="is-current">HOME</li><li>ABOUT US</li><li>OUR PRODUCTS</li><li>LATEST BLOG</li><li>CONTACT US</li>
  </ul>
  <div class="footer-sep" style="left:136px"></div>

  <h3 class="footer-col-title" style="left:159px">CONTACT <span>DETAILS</span></h3>
  <div class="footer-rule" style="left:159px;width:130px"></div>
  <div class="contact-name">Pimbrox Inc.</div>
  <div class="contact-addr">123, Lorem Ipsum Dollar Smit Amet,<br>Nibh Nonumy. Golham - 123 456</div>
  <div class="contact-row" style="top:101px"><svg width="9" height="9" viewBox="0 0 11 11"><path d="M2 1l2 0 1 3-1.5 1a6 6 0 0 0 3 3L7.5 6.5l3 1 0 2c-5 1-9.5-3.5-8.5-8.5z" fill="#7aad3a"/></svg>123 456 7890</div>
  <div class="contact-row" style="top:120px"><svg width="9" height="9" viewBox="0 0 10 10"><rect x="2.5" y="0.5" width="5" height="3" fill="#7aad3a"/><rect x="0.5" y="3.5" width="9" height="4" fill="#7aad3a"/><rect x="2.5" y="6.5" width="5" height="3" fill="#7aad3a"/></svg>123 456 7890</div>
  <div class="contact-row" style="top:139px"><svg width="9" height="8" viewBox="0 0 10 8"><rect width="10" height="8" fill="#7aad3a"/><polyline points="0,0 5,4 10,0" fill="none" stroke="#262626" stroke-width=".8"/></svg>info@pimbroxinc.com</div>
  <div class="footer-sep" style="left:297px"></div>

  <h3 class="footer-col-title" style="left:321px">LOCATION <span>MAP</span></h3>
  <div class="footer-rule" style="left:321px;width:143px"></div>
  <div class="map" role="img" aria-label="Street map showing the office location"></div>
  <div class="footer-sep" style="left:476px"></div>

  <div class="footer-brand"><span class="footer-brand-mark"></span>Pimbrox</div>
</footer>

<div class="bottom-bar">
  <span class="copyright">Copyright © 2016 Pimbroxinc. All Rights Reserved.</span>
  <span class="follow">Follow Us :</span>
  <span class="social" style="left:525px;background:#3b5a9a"></span>
  <span class="social" style="left:550px;background:#3aa1d8"></span>
  <span class="social" style="left:575px;background:#1b77b3"></span>
  <span class="social" style="left:600px;background:#c8322b"></span>
</div>

</body>
</html>
```